Cover-Design für Collegeblockserie
Zielgruppe
Wir sind ein Anbieter von Papierprodukten wie Hefte, Collegeblöcke und gebundene Bücher für den Schul- und Officebereich. In jedem Jahr bringne wir eine Collegeblockserie heraus mit einem limitierten Coverdesign.
Weitere Infos zu uns und der Aufgabe können dem beigefügten Briefing entnommen werden.
Aufgabenstellung
Vorgaben können dem Breifing entnommen werden

```html
<!DOCTYPE html>
<html lang="en">
<head>
<meta charset="utf-8">
<title>Power in your hands – College Block Cover Series</title>
<link rel="stylesheet" href="https://fonts.googleapis.com/css2?family=Permanent+Marker&family=Roboto+Slab:wght@700&display=swap">
<style>
  :root {
    --stage: #e8e8ec;
    --cover-shadow: rgba(40, 30, 60, 0.22);
    --violet-deep: #6f5be0;
    --violet-soft: #b8a8ee;
    --ice: #dff0f6;
    --lilac: #cdb6ec;
    --navy-ink: #2b2a6e;
    --pink-hot: #ee7fd4;
    --pink-soft: #f6c9e4;
    --blush: #f4a3b3;
    --mauve: #c9b3e6;
    --plum-ink: #5a2552;
    --rose: #f08fb8;
  }
  * { margin: 0; padding: 0; box-sizing: border-box; }
  html, body {
    width: 1200px;
    height: 800px;
    overflow: hidden;
    background: var(--stage);
  }
  .stage {
    position: relative;
    width: 1200px;
    height: 800px;
    display: flex;
    justify-content: center;
    align-items: center;
    gap: 90px;
  }
  .cover {
    position: relative;
    width: 470px;
    height: 620px;
    overflow: hidden;
    box-shadow: 0 14px 34px var(--cover-shadow);
  }
  .cover__wash {
    position: absolute;
    inset: 0;
  }
  .cover--violet .cover__wash {
    background:
      radial-gradient(ellipse 60% 40% at 80% 8%, var(--violet-deep) 0%, transparent 70%),
      radial-gradient(ellipse 55% 45% at 20% 85%, var(--violet-soft) 0%, transparent 75%),
      radial-gradient(ellipse 70% 50% at 60% 45%, var(--ice) 0%, transparent 80%),
      linear-gradient(160deg, var(--lilac) 0%, var(--ice) 45%, var(--violet-soft) 100%);
  }
  .cover--rose .cover__wash {
    background:
      radial-gradient(ellipse 55% 35% at 85% 5%, var(--pink-hot) 0%, transparent 70%),
      radial-gradient(ellipse 50% 40% at 15% 80%, var(--pink-hot) 0%, transparent 75%),
      radial-gradient(ellipse 70% 50% at 60% 50%, #f3ecf7 0%, transparent 80%),
      linear-gradient(160deg, var(--pink-soft) 0%, #efe6f5 45%, var(--mauve) 100%);
  }
  .cover__flowers {
    position: absolute;
    border-radius: 50%;
    filter: blur(6px);
  }
  .cover--violet .cover__flowers--top {
    left: -40px; top: -40px; width: 230px; height: 150px;
    background: radial-gradient(circle, #c46ee0 0%, rgba(196,110,224,0.4) 55%, transparent 75%);
  }
  .cover--rose .cover__flowers--top {
    left: -40px; top: -50px; width: 260px; height: 150px;
    background: radial-gradient(circle, var(--blush) 0%, rgba(244,163,179,0.45) 55%, transparent 75%);
  }
  .cover--rose .cover__flowers--bottom {
    right: -70px; bottom: -60px; width: 300px; height: 330px;
    background: radial-gradient(circle, var(--rose) 0%, rgba(240,143,184,0.5) 55%, transparent 75%);
  }
  .brand {
    position: absolute;
    left: 58px;
    top: 52px;
    display: flex;
    align-items: center;
    gap: 10px;
  }
  .brand__mark {
    width: 22px;
    height: 22px;
    background: var(--navy-ink);
  }
  .brand__name {
    font-family: 'Permanent Marker', cursive;
    font-size: 30px;
    color: var(--navy-ink);
    letter-spacing: 1px;
  }
  .cover__headline {
    position: absolute;
    left: 0;
    right: 0;
    top: 220px;
    text-align: center;
    font-family: 'Permanent Marker', cursive;
    font-weight: 400;
    font-size: 62px;
    line-height: 1.2;
    letter-spacing: 1px;
  }
  .cover--violet .cover__headline { color: var(--navy-ink); }
  .cover--rose .cover__headline { color: var(--plum-ink); }
</style>
</head>
<body>
  <main class="stage">
    <section class="cover cover--violet">
      <div class="cover__wash" role="img" aria-label="Blue and violet watercolour wash with drifting flower petals"></div>
      <div class="cover__flowers cover__flowers--top" role="img" aria-label="Violet watercolour flower in the top corner"></div>
      <div class="brand">
        <span class="brand__mark"></span>
        <span class="brand__name">Lindmark</span>
      </div>
      <h1 class="cover__headline">POWER IN<br>YOUR HANDS</h1>
    </section>

    <section class="cover cover--rose">
      <div class="cover__wash" role="img" aria-label="Pink and lilac watercolour wash with drifting rose petals"></div>
      <div class="cover__flowers cover__flowers--top" role="img" aria-label="Coral watercolour flower in the top corner"></div>
      <div class="cover__flowers cover__flowers--bottom" role="img" aria-label="Pink watercolour rose in the bottom corner"></div>
      <div class="brand">
        <span class="brand__mark"></span>
        <span class="brand__name">Lindmark</span>
      </div>
      <h1 class="cover__headline">POWER IN<br>YOUR HANDS</h1>
    </section>
  </main>
</body>
</html>
```